Need a sleek, professional business card design for a Web Development business

I need a unique business card designed for a web development company. It is also the parent company for any ventures I do, such as my ClipWave channel, startup ideas I have, etc. I am the single member of "Bright Harbor Code LLC." I will attach my basic logo here, so you will see the current color scheme and have the asset available. Thank you!

Target Market(s)

Startups, SMB's, Professionals

Industry/Entity Type

Business

Font styles to use
Other font styles liked:
• Lovello for headings is what I use, but not necessary.

Colors

Designer to choose colors to be used in the design.

Requirements
Nice to have
• Sleek is the word. Professional, modern, dark.
Should not have
• Any work from someone else's design. Lacking originality.

```html
<!DOCTYPE html>
<html lang="en">
<head>
<meta charset="utf-8">
<title>Bright Harbor Code LLC — Business Card</title>
<link rel="stylesheet" href="https://fonts.googleapis.com/css2?family=Josefin+Sans:wght@700&family=Arimo:wght@400&display=swap">
<style>
  :root {
    --page: #ffffff;
    --ink: #1f1f1f;
    --panel-dark: #1e1e1e;
    --peach: #f7a062;
    --warm-light: #f9a75e;
    --warm-mid: #f38a64;
    --warm-deep: #ec6a68;
    --icon-line: #f4885f;
  }
  * { box-sizing: border-box; margin: 0; padding: 0; }
  html, body {
    width: 1200px;
    height: 1000px;
    overflow: hidden;
    background: var(--page);
  }
  .card {
    position: absolute;
    left: 139px;
    top: 222px;
    width: 921px;
    height: 527px;
    background: linear-gradient(45deg, var(--warm-light) 0%, var(--warm-mid) 55%, var(--warm-deep) 100%);
    overflow: hidden;
  }
  .brand-panel {
    position: absolute;
    left: 0;
    top: 0;
    width: 370px;
    height: 100%;
    background: var(--panel-dark);
  }
  .brand-square {
    position: absolute;
    left: 130px;
    top: 118px;
    width: 110px;
    height: 110px;
    background: var(--peach);
  }
  .brand-name {
    position: absolute;
    left: 0;
    top: 318px;
    width: 100%;
    text-align: center;
    font-family: "Josefin Sans", sans-serif;
    font-weight: 700;
    font-size: 31px;
    line-height: 44px;
    letter-spacing: 3px;
    color: var(--peach);
    text-transform: uppercase;
  }
  .accent-left {
    position: absolute;
    left: 0;
    bottom: 0;
    width: 10px;
    height: 70px;
    background: var(--warm-mid);
  }
  .accent-right {
    position: absolute;
    right: 0;
    top: 0;
    width: 13px;
    height: 68px;
    background: var(--panel-dark);
  }
  .person-name {
    position: absolute;
    right: 59px;
    top: 112px;
    font-family: "Josefin Sans", sans-serif;
    font-weight: 700;
    font-size: 60px;
    line-height: 62px;
    letter-spacing: 2px;
    color: var(--ink);
    text-transform: uppercase;
    white-space: nowrap;
  }
  .contact-list {
    position: absolute;
    right: 64px;
    top: 0;
    list-style: none;
  }
  .contact-item {
    position: absolute;
    right: 0;
    display: flex;
    align-items: center;
    gap: 22px;
    transform: translateY(-50%);
  }
  .contact-item--phone { top: 286px; }
  .contact-item--mail { top: 363px; }
  .contact-item--place { top: 440px; }
  .contact-text {
    font-family: "Arimo", sans-serif;
    font-size: 22px;
    line-height: 29px;
    letter-spacing: 0.6px;
    color: var(--ink);
    text-align: right;
    white-space: nowrap;
  }
  .contact-icon {
    width: 54px;
    height: 54px;
    border-radius: 50%;
    background: var(--panel-dark);
    display: flex;
    align-items: center;
    justify-content: center;
    flex: none;
  }
  .contact-icon svg { width: 28px; height: 28px; }
</style>
</head>
<body>
  <div class="card">
    <section class="brand-panel">
      <div class="brand-square"></div>
      <p class="brand-name">Bright Harbor<br>Code LLC</p>
    </section>
    <div class="accent-left"></div>
    <div class="accent-right"></div>

    <h1 class="person-name">Evan Rowe</h1>

    <ul class="contact-list">
      <li class="contact-item contact-item--phone">
        <p class="contact-text">+555 204 318 6627<br>+555 204 318 6628</p>
        <span class="contact-icon">
          <svg viewBox="0 0 24 24" fill="none" stroke="var(--icon-line)" stroke-width="1.8" stroke-linecap="round" stroke-linejoin="round">
            <path d="M5 4h3l1.5 4-2 1.3a11 11 0 0 0 7.2 7.2l1.3-2 4 1.5v3a2 2 0 0 1-2 2A16 16 0 0 1 3 6a2 2 0 0 1 2-2z"/>
            <path d="M14 3.5a6.5 6.5 0 0 1 6.5 6.5"/>
            <path d="M14 7a3 3 0 0 1 3 3"/>
          </svg>
        </span>
      </li>
      <li class="contact-item contact-item--mail">
        <p class="contact-text">hello@brightharbor.dev<br>admin@brightharbor.dev</p>
        <span class="contact-icon">
          <svg viewBox="0 0 24 24" fill="none" stroke="var(--icon-line)" stroke-width="1.8" stroke-linejoin="round">
            <rect x="3" y="6" width="18" height="12"/>
            <path d="M3 6l9 7 9-7"/>
            <path d="M3 18l7-6M21 18l-7-6"/>
          </svg>
        </span>
      </li>
      <li class="contact-item contact-item--place">
        <p class="contact-text">Lorem ipsum dolor<br>sit amet consectetur</p>
        <span class="contact-icon">
          <svg viewBox="0 0 24 24" fill="none" stroke="var(--icon-line)" stroke-width="1.8" stroke-linejoin="round">
            <path d="M12 22s-7-7.5-7-12.5a7 7 0 0 1 14 0C19 14.5 12 22 12 22z"/>
            <circle cx="12" cy="9.5" r="2.6"/>
          </svg>
        </span>
      </li>
    </ul>
  </div>
</body>
</html>
```